Modern Label Design needed for Virgin Coconut Oil bottle

Label for organic virgin coconut oil. Must be unique, creative, modern and give the impression of an expensive premium product.
Label is for round containers (bottles and jars) 250 ml, 500 ml and 750 ml.
The Brand name is "Mont Verane" and the product stated must include the words "organic" "cold-pressed" and "virgin coconut oil".
Label must include the following product description:
"Mont Verane virgin coconut oil is made from fresh mature coconuts harvested from organic farms across the Caribbean region. The oil is produced using the traditional natural fermentation method. Absolutely no heat is used in the process to allow for the maximum possible content of lauric acid."
Additional info: "Product of Tobago" "Manufactured and bottled by Sunmere Harvest Ltd., Barrow Agro-Commercial Estate, Lowlands Tobago".
Label must include room for Best Before date, Batch number, barcode and nutrition facts.
Colors can be at designer's discretion. However white, green and gold are preferred.

Target Market(s)

Women, Cosmetic Industry, (Food Industry to a lesser extent)

Industry/Entity Type

Product

Font styles to use
Script

Requirements
Must have
• An expensive look.
• The label is intended to have a transparent background
Nice to have
• The colors green and gold. However other color suggestions are welcome.
• Also, tasteful images that communicate an exotic tropical environment. (flowers, palms, coconuts

```html
<!DOCTYPE html>
<html lang="en">
<head>
<meta charset="utf-8">
<title>Mont Verane Virgin Coconut Oil Label</title>
<link rel="stylesheet" href="https://fonts.googleapis.com/css2?family=Montserrat:wght@400;500;600&family=Yellowtail&display=swap">
<style>
  :root {
    --bg: #ffffff;
    --ink: #3a3a3a;
    --body-ink: #3d3d3d;
    --accent: #f28a1e;
    --mark-grey: #e3e3e3;
    --box-line: #b9b9b9;
  }
  * { margin: 0; padding: 0; box-sizing: border-box; }
  html, body {
    width: 1200px;
    height: 1200px;
    overflow: hidden;
    background: var(--bg);
  }
  .label {
    width: 1200px;
    height: 1200px;
    display: flex;
    flex-direction: column;
    align-items: center;
    padding-top: 120px;
    font-family: "Montserrat", sans-serif;
    color: var(--ink);
  }
  .brand-mark {
    width: 290px;
    height: 290px;
    border-radius: 50%;
    background: var(--mark-grey);
  }
  .brand-name {
    margin-top: 56px;
    font-size: 92px;
    font-weight: 500;
    line-height: 1;
    letter-spacing: -1px;
    color: var(--ink);
  }
  .product-claim {
    margin-top: 22px;
    font-size: 30px;
    font-weight: 600;
    line-height: 1.1;
  }
  .product-type {
    margin-top: 10px;
    font-size: 26px;
    font-weight: 500;
    letter-spacing: 3.5px;
    line-height: 1.1;
  }
  .origin {
    margin-top: 30px;
    font-family: "Yellowtail", cursive;
    font-size: 52px;
    color: var(--accent);
    line-height: 1;
  }
  .volume {
    margin-top: 34px;
    font-size: 38px;
    font-weight: 400;
    color: var(--accent);
    line-height: 1;
  }
  .description {
    margin-top: 24px;
    width: 676px;
    border: 1px solid var(--box-line);
    padding: 10px 10px 12px 11px;
    font-size: 20.4px;
    line-height: 1.6;
    color: var(--body-ink);
    font-weight: 400;
  }
</style>
</head>
<body>
  <main class="label">
    <div class="brand-mark" aria-hidden="true"></div>
    <h1 class="brand-name">Mont Verane</h1>
    <p class="product-claim">organic, cold-pressed</p>
    <p class="product-type">VIRGIN COCONUT OIL</p>
    <p class="origin">Product of Tobago</p>
    <p class="volume">250 ml</p>
    <p class="description">Mont Verane virgin coconut oil is made from fresh mature coconuts harvested from organic farms across the Caribbean region. The oil is produced using the traditional natural fermentation method. Absolutely no heat is used in the process to allow for the maxim-<br>-um possible content of lauric acid</p>
  </main>
</body>
</html>
```